依頼詳細
ロゴはミナモワークスで作成していただいていますので、それを使用していただいきたいです。ホームページは現在作成中です。ロゴを取り入れ、柔らかい雰囲気でシンプルなイメージ、わかりやすい感じがいいです。
記載項目
病院名、ロゴ、開業日、内覧会の日程、住所、電話番号、ホームページのアドレス、診察時間、休診日 対象動物、挨拶等
サイズ
A4
ページ数
片面
希望イメージ
シンプル 複雑
単色 カラフル
暗い 明るい
日常 高級
遊び心 厳粛
未来的 伝統的
女性的 男性的
希望する色
納品ファイル
補足説明
ロゴを添付します。

挨拶内容
「はじめまして、はるかぜペットクリニック院長の森岡健司です。大学卒業後、熊本市内の動物病院で7年間勤務し、2014年3月24日に動物病院を開院することになりました。
ホームドクターとして地域の皆様に親しまれる病院であるとともに、飼い主様と一緒に家族である動物たちの最善のケアができるように努めてまいりたいと思います。ワンちゃん達が遊べるスペースも少しですが用意してあります。ぜひ気軽に遊びにいらしてください。今後ともよろしくお願い致します。」
おそくなりましたが、ホームページのドメイン決まりました。
http://harukaze-petclinic.exampleです。
よろしくお願いいたします。
■ 選んだ理由

シンプルで開院ということがわかりやすかったため。
犬の写真の雰囲気も良かったです。

■ 提案者全員のお礼・コメント

いいデザインを多数いただいてありがとうございます。それぞれおもしろくけっこう悩ませていただきました。また、よろしくお願いいたします。

```html
<!DOCTYPE html>
<html lang="ja">
<head>
<meta charset="utf-8">
<title>はるかぜペットクリニック 開院のお知らせ</title>
<link href="https://fonts.googleapis.com/css2?family=M+PLUS+Rounded+1c:wght@400;500;700;800&display=swap" rel="stylesheet">
<style>
  :root {
    --yellow: #fdd94d;
    --yellow-soft: #fff3b8;
    --cream: #fffdf2;
    --orange: #f29418;
    --orange-dark: #e07b0c;
    --red-orange: #e94e1b;
    --teal: #1d86b8;
    --brown: #5a4632;
    --pink: #f7a8bd;
    --white: #ffffff;
    --silhouette: #ffffff;
    --map: #cfe3ef;
  }
  * { margin: 0; padding: 0; box-sizing: border-box; }
  html, body { width: 848px; height: 1200px; overflow: hidden; background: #eeeeee; }
  body { font-family: "M PLUS Rounded 1c", sans-serif; color: var(--brown); }
  .flyer { position: relative; width: 848px; height: 1200px; background: var(--yellow); overflow: hidden; }

  .opening { position: absolute; left: 0; top: 0; width: 848px; height: 240px; }
  .opening-date { position: absolute; left: 40px; top: 26px; color: var(--orange-dark); font-weight: 800; font-size: 64px; letter-spacing: 2px; white-space: nowrap; }
  .opening-date small { font-size: 40px; }
  .opening-word { position: absolute; left: 230px; top: 112px; color: var(--red-orange); font-weight: 800; font-size: 82px; letter-spacing: 6px; }

  .preview { position: absolute; right: 34px; top: 28px; width: 196px; height: 200px; background: var(--white); border-radius: 14px; overflow: hidden; text-align: center; }
  .preview-title { background: var(--orange); color: var(--white); font-weight: 700; font-size: 24px; padding: 8px 0; letter-spacing: 3px; }
  .preview-days { color: var(--red-orange); font-weight: 800; font-size: 27px; margin-top: 10px; white-space: nowrap; }
  .preview-days span { font-size: 15px; }
  .preview-time { font-weight: 700; font-size: 22px; margin-top: 4px; }
  .preview-note { color: var(--red-orange); font-size: 14px; font-weight: 700; margin-top: 8px; line-height: 1.3; }

  .brand { position: absolute; left: 0; top: 240px; width: 848px; height: 220px; background: var(--white); text-align: center; }
  .brand-mark { display: block; margin: 34px auto 16px; width: 70px; height: 70px; border-radius: 50%; background: var(--teal); }
  .brand-name { color: var(--teal); font-weight: 700; font-size: 40px; letter-spacing: 3px; }
  .brand-roman { color: var(--teal); font-weight: 700; font-size: 18px; letter-spacing: 2px; margin-top: 2px; }

  .greeting { position: absolute; left: 0; top: 460px; width: 848px; height: 300px; }
  .greeting-photo { position: absolute; left: 44px; top: 40px; width: 150px; height: 150px; border-radius: 50%; background: var(--pink); }
  .greeting-heading { position: absolute; left: 236px; top: 30px; width: 380px; height: 42px; border-radius: 21px; background: var(--white); color: var(--orange-dark); font-weight: 700; font-size: 22px; text-align: center; line-height: 42px; letter-spacing: 4px; }
  .greeting-text { position: absolute; left: 236px; top: 88px; width: 390px; font-size: 15px; line-height: 1.65; font-weight: 500; text-align: center; }
  .cat-art { position: absolute; left: 30px; top: 215px; width: 160px; height: 80px; border-radius: 40px 40px 6px 6px; background: var(--silhouette); opacity: .85; }
  .dog-art { position: absolute; right: 40px; top: 110px; width: 160px; height: 180px; border-radius: 60px 60px 8px 8px; background: var(--silhouette); opacity: .85; }

  .info { position: absolute; left: 0; top: 760px; width: 848px; height: 440px; background: var(--cream); }
  .map { position: absolute; left: 28px; top: 36px; width: 262px; height: 250px; background: var(--map); border: 4px solid var(--orange); border-radius: 6px; }
  .contact-heading, .hours-heading { position: absolute; height: 36px; border-radius: 18px; background: var(--yellow); color: var(--orange-dark); font-weight: 700; font-size: 19px; text-align: center; line-height: 36px; letter-spacing: 3px; }
  .contact-heading { left: 312px; top: 36px; width: 210px; }
  .contact-tel { position: absolute; left: 312px; top: 96px; width: 300px; color: var(--orange-dark); font-weight: 800; font-size: 26px; letter-spacing: 0; display: flex; align-items: center; gap: 6px; white-space: nowrap; }
  .contact-tel svg { width: 24px; height: 24px; flex: none; }
  .contact-detail { position: absolute; left: 312px; top: 150px; width: 306px; font-size: 14px; line-height: 1.8; }

  .hours-heading { left: 636px; top: 36px; width: 184px; }
  .hours { position: absolute; left: 636px; top: 84px; width: 184px; border-collapse: collapse; font-size: 14px; }
  .hours th, .hours td { border-bottom: 1px dashed var(--orange); padding: 8px 2px; text-align: center; vertical-align: middle; white-space: nowrap; }
  .hours th { width: 52px; font-weight: 700; }
  .hours td { line-height: 1.5; font-size: 13px; }

  .species { position: absolute; left: 28px; top: 340px; width: 792px; font-size: 26px; font-weight: 800; color: var(--orange-dark); letter-spacing: 2px; text-align: center; }
  .species span { font-size: 17px; font-weight: 500; color: var(--brown); }
</style>
</head>
<body>
<div class="flyer">
  <header class="opening">
    <div class="opening-date">2014<small>年</small> 3<small>月</small>24<small>日</small></div>
    <div class="opening-word">OPEN!</div>
    <aside class="preview">
      <div class="preview-title">内覧会</div>
      <div class="preview-days">3/21<span>(金)</span> / 22<span>(土)</span></div>
      <div class="preview-time">10:00 ～ 17:00</div>
      <div class="preview-note">お気軽に<br>おこしください!</div>
    </aside>
  </header>

  <section class="brand">
    <span class="brand-mark"></span>
    <div class="brand-name">はるかぜペットクリニック</div>
    <div class="brand-roman">Harukaze Pet Clinic</div>
  </section>

  <section class="greeting">
    <div class="greeting-photo" role="img" aria-label="院長の写真"></div>
    <h2 class="greeting-heading">はじめまして</h2>
    <p class="greeting-text">はるかぜペットクリニック院長の森岡健司です。大学卒業後、熊本市内の動物病院で7年間勤務し、2014年3月24日に動物病院を開院することになりました。ホームドクターとして地域の皆様に親しまれる病院であるとともに、飼い主様と一緒に家族である動物たちの最善のケアができるように努めてまいりたいと思います。ワンちゃん達が遊べるスペースも少しですが用意してあります。ぜひ気軽に遊びにいらしてください。今後ともよろしくお願い致します。</p>
    <div class="cat-art" role="img" aria-label="歩く猫のシルエットイラスト"></div>
    <div class="dog-art" role="img" aria-label="座る犬のシルエットイラスト"></div>
  </section>

  <section class="info">
    <div class="map" role="img" aria-label="クリニック周辺の地図"></div>

    <h3 class="contact-heading">お問い合わせ</h3>
    <div class="contact-tel">
      <svg viewBox="0 0 24 24" aria-hidden="true"><path fill="currentColor" d="M6.6 10.8a15.1 15.1 0 0 0 6.6 6.6l2.2-2.2c.3-.3.7-.4 1-.2 1.1.4 2.3.6 3.6.6.6 0 1 .4 1 1V20c0 .6-.4 1-1 1A17 17 0 0 1 3 4c0-.6.4-1 1-1h3.5c.6 0 1 .4 1 1 0 1.3.2 2.5.6 3.6.1.3 0 .7-.2 1z"/></svg>
      TEL 096-000-1234
    </div>
    <div class="contact-detail">
      FAX 096-000-1235<br>
      熊本市東区みどり台4丁目11-126<br>
      ホームページ<br>http://harukaze-petclinic.example
    </div>

    <h3 class="hours-heading">診療時間</h3>
    <table class="hours">
      <tr><th>月～金</th><td>午前 9:00～12:00<br>午後 16:00～19:00</td></tr>
      <tr><th>土</th><td>午前 9:00～12:00<br>午後 14:00～17:00</td></tr>
      <tr><th>日・祝</th><td>休診</td></tr>
    </table>

    <p class="species">対象動物：犬、猫、ウサギ、ハムスター <span>など</span></p>
  </section>
</div>
</body>
</html>
```